Premium Business Workbook / PDF Handbook Design

We need a premium business workbook / PDF handbook design for our brand, Brightloom.

All written content is complete. Your role is to elevate the document visually layout, typography, hierarchy, and flow, so it feels modern, authoritative and high-end. (please remove all em dashs when inserting text)

Quality benchmark: Rob Kessing–style business workbooks (clean, bold, structured, not templated).

Deliverable: a professionally designed, print- and digital-ready PDF that is easy to read, easy to use, and reinforces a premium brand.

Brand guidelines, content, and reference examples will be provided.

Link to our branding kit:
https://files.quillnest.net/folders/7tkwpRz2LmQa9XcV4bN8yHd3Je6UfKsTo?share=open

https://files.quillnest.net/file/d/5w_k3ZtPmYbn8CrLx2Gd7Hq9VeAsJfMoN/view?share=open

```html
<!DOCTYPE html>
<html lang="en">
<head>
<meta charset="utf-8">
<title>The 90-Day Business Accelerator Method | Brightloom</title>
<link rel="stylesheet" href="https://fonts.googleapis.com/css2?family=Barlow+Condensed:ital,wght@1,700;1,800;1,900&family=Inter:wght@400;500;600;700;800&display=swap">
<style>
:root{
  --yellow:#f3ee6d;
  --yellow-deep:#e9e35f;
  --ink:#232323;
  --ink-soft:#2e2e2e;
  --paper:#ffffff;
  --mist:#ebebeb;
  --board:#e4e4e4;
  --text:#2a2a2a;
  --red:#c0272d;
  --green:#2e8b3a;
  --head:"Barlow Condensed", "Arial Narrow", sans-serif;
  --body:"Inter", "Helvetica Neue", Arial, sans-serif;
}
*{box-sizing:border-box;margin:0;padding:0}
html,body{width:1200px;height:2918px;overflow:hidden;background:var(--board)}
.board{position:relative;width:1200px;height:2918px;background:var(--board);font-family:var(--body);color:var(--text)}
.page{position:absolute;width:561px;height:395px;overflow:hidden;background:var(--paper)}
.col-a{left:32px}.col-b{left:607px}
.row-1{top:32px}.row-2{top:441px}.row-3{top:850px}.row-4{top:1259px}.row-5{top:1668px}.row-6{top:2077px}.row-7{top:2486px}
.abs{position:absolute}
.fill{position:absolute;inset:0}
.yellow{background:var(--yellow)}
.ink{background:var(--ink)}
.mist{background:var(--mist)}
.display{font-family:var(--head);font-style:italic;font-weight:900;text-transform:uppercase;line-height:.92;letter-spacing:-.5px}
.band{position:absolute;left:0;top:0;height:54px;background:var(--ink);color:var(--paper);display:flex;align-items:center;padding-left:36px;font-family:var(--head);font-style:italic;font-weight:800;text-transform:uppercase;font-size:29px;letter-spacing:-.3px}
.copy{font-size:8.6px;line-height:1.32;color:var(--text)}
.copy p{margin-bottom:6px}
.copy.light{color:#f1f1f1}
.copy b{font-weight:700}
.label{font-size:9.6px;font-weight:700;text-transform:uppercase;letter-spacing:.2px;color:var(--ink)}
.dots{list-style:none}
.dots li{position:relative;padding-left:11px;margin-bottom:4px;font-size:8.6px;line-height:1.28}
.dots li::before{content:"";position:absolute;left:0;top:3px;width:6px;height:6px;border-radius:50%;background:var(--ink)}
.dots.on-dark li{color:#f1f1f1}
.dots.on-dark li::before{background:var(--yellow)}
.dots.big li{font-size:11px;font-weight:700;margin-bottom:15px;padding-left:13px}
.dots.big li::before{top:3.5px;width:7px;height:7px}
.brand{position:absolute;left:36px;bottom:22px;display:flex;align-items:center;gap:5px;font-family:var(--body);font-weight:800;font-size:12px;letter-spacing:.4px;text-transform:uppercase;color:var(--ink)}
.brand::before{content:"";width:14px;height:14px;background:currentColor}
.brand.reverse{color:var(--paper)}
.folio{position:absolute;right:26px;bottom:20px;font-size:8px;color:var(--ink)}
.folio.reverse{color:#ddd}
.photo{position:absolute}
.step-rail{position:absolute;left:0;top:0;width:135px;height:395px}
.step-tag{position:absolute;left:10px;top:18px;writing-mode:vertical-rl;transform:rotate(180deg);font-family:var(--head);font-style:italic;font-weight:900;font-size:25px;color:var(--yellow);letter-spacing:.5px}
.num-list{list-style:none}
.num-list li{display:flex;gap:7px;align-items:flex-start;font-size:11.4px;font-weight:700;line-height:1.15;margin-bottom:11px;color:var(--ink)}
.num-list li span{flex:0 0 16px;height:16px;border-radius:50%;background:var(--ink);color:var(--yellow);font-size:9px;display:flex;align-items:center;justify-content:center}
.stat-card{position:absolute;background:var(--yellow);padding:10px 10px 0 14px}
.stat-card .copy{margin-bottom:8px}
.stage{position:absolute;font-size:8.4px;line-height:1.25;color:#eee}
.stage .k{color:var(--yellow);font-weight:800;text-transform:uppercase;font-size:8.6px}
.stage b{color:#fff;font-weight:700}
</style>
</head>
<body>
<main class="board">

<!-- 1 Cover -->
<section class="page col-a row-1 yellow">
  <div class="photo" role="img" aria-label="Decorative tonal pattern band" style="left:262px;top:0;width:299px;height:104px;background:linear-gradient(90deg,var(--yellow),var(--yellow-deep))"></div>
  <div class="abs display" style="left:36px;top:26px;font-size:58px;color:var(--ink)">
    <span style="display:inline-block;font-size:15px;writing-mode:vertical-rl;transform:rotate(180deg);vertical-align:top;margin:6px 2px 0 0">THE</span>90-DAY<br>BUSINESS ACCELERATOR<br>METHOD
  </div>
  <svg class="abs" style="left:0;top:0" width="561" height="395" aria-hidden="true"><polygon points="292,158 561,158 561,395 204,395" fill="#232323"/></svg>
  <div class="abs label" style="left:36px;top:245px;width:170px;line-height:1.3;font-size:9.8px">
    <p style="margin-bottom:14px">Double your profitability.</p>
    <p style="margin-bottom:14px">Get 20-30 hours a week<br>of your time back.</p>
    <p>Without burning out your business, your marriage, or yourself.</p>
  </div>
  <div class="abs copy light" style="left:272px;top:212px;width:262px;text-align:center">
    <p>Built for established business owners who look successful on the outside - but are drowning behind the scenes.</p>
    <p>This method is for owners who love business, mean well, and got into it for freedom - yet feel trapped by a company that depends entirely on them.</p>
    <p>If this works, in 90 days you'll finally feel hope again. You'll see how to grow a profitable business and be a present parent, partner, and leader - with the ability to step away without stress.</p>
    <p style="margin-bottom:0">This isn't theory.<br>It's built from a proven track record of building five successful companies and helping 940+ Australian businesses grow while getting their time back - with documented, measured results year on year.</p>
  </div>
  <div class="brand">Brightloom</div>
</section>

<!-- 2 Read this first -->
<section class="page col-b row-1">
  <svg class="abs" style="left:0;top:0" width="561" height="395" aria-hidden="true">
    <polygon points="300,0 561,0 561,395 262,395" fill="#f3ee6d"/>
    <polygon points="0,0 302,0 296,54 0,54" fill="#232323"/>
    <polygon points="292,55 561,55 561,110 286,110" fill="#232323"/>
  </svg>
  <div class="abs display" style="left:36px;top:15px;font-size:25px;color:#fff;font-weight:800">Read this first</div>
  <div class="abs display" style="left:334px;top:70px;font-size:25px;color:#fff;font-weight:800">Who this is <span style="color:var(--yellow)">not</span> for</div>
  <div class="abs copy" style="left:36px;top:75px;width:232px">
    <p>This method is for business owners working 80-hour weeks while telling themselves, <i>"It's just for now."</i></p>
    <p>Yet somehow, their kids are always asleep by the time they get home.</p>
    <p>It's for owners who have missed birthdays, dinners, school events, and weekends because the business always needs <i>one more thing.</i></p>
    <p>You don't want to wake up in five years and realise you built a successful business at the expense of the people you were doing it for.</p>
    <p>You know something has to change - but you don't want hype, motivation, or surface-level advice.</p>
    <p>You want clarity.<br>You want direction.<br>You want a plan that actually works.</p>
  </div>
  <div class="abs copy" style="left:296px;top:128px;width:238px;text-align:center">
    <p>This is not for business owners looking for a quick fix or a magic pill.</p>
    <p>It's not for those who are comfortable letting their marriage slowly fall apart because work always comes first.</p>
    <p>It's not for people who enjoy stress, chaos, impatience, or being hard to be around.</p>
    <p>And it's definitely not for anyone willing to tolerate a life they secretly hate.</p>
    <p>This is general strategic guidance, not personalised advice.</p>
    <p>It won't fix your business for you - but it will show you exactly where to start.</p>
  </div>
  <div class="brand">Brightloom</div>
  <div class="folio">2</div>
</section>

<!-- 3 Core problem -->
<section class="page col-a row-2 yellow">
  <div class="photo" role="img" aria-label="Dim corridor photo with a lone figure walking away" style="left:0;top:0;width:300px;height:395px;clip-path:polygon(0 0,100% 0,80% 100%,0 100%);background:radial-gradient(ellipse at 62% 40%,#4a4a44 0%,#262624 45%,#121212 100%)"></div>
  <div class="abs display" style="left:192px;top:34px;font-size:54px;color:var(--yellow)">The</div>
  <div class="abs display" style="left:303px;top:34px;font-size:54px;color:var(--ink)">Core<br>Problem</div>
  <div class="abs" style="left:36px;top:152px;width:200px;color:#fff;font-size:14.4px;font-weight:500;text-transform:uppercase;line-height:1.65;letter-spacing:.3px">Most business owners don't fail - they lose themselves along the way.</div>
  <div class="abs copy" style="left:270px;top:150px;width:272px;text-align:center;line-height:1.35">
    They don't wake up one day and fail.<br>They drift.<br>They live life on default instead of by design.<br>Low energy.<br>Reactive.<br>No clear plan - just putting out fires.<br>They expect level-10 output from their team,<br>while showing up as a level-6 leader themselves.<br>They question their team.<br>Then they question their business.<br>Eventually, they question themselves.<br>Not because they're incapable - but because they've lost clarity, belief, and direction.<br>Surrounded by other stressed business owners, dysfunction becomes normal.<br>This isn't a failure problem.<br>It's a <b>strategy, belief, and leadership problem.</b>
  </div>
  <div class="brand reverse">Brightloom</div>
  <div class="folio">3</div>
</section>

<!-- 4 The method -->
<section class="page col-b row-2">
  <svg class="abs" style="left:0;top:0" width="561" height="395" aria-hidden="true">
    <polygon points="326,0 561,0 561,395 262,395" fill="#2b2b2b"/>
    <polygon points="296,0 330,0 272,342 238,342" fill="#f3ee6d"/>
    <polygon points="214,334 298,348 242,397" fill="#f3ee6d"/>
    <g fill="#3a3a3a" stroke="#e0dcc0" stroke-width="2">
      <circle cx="294" cy="120" r="11"/><circle cx="286" cy="176" r="11"/><circle cx="278" cy="221" r="11"/><circle cx="270" cy="265" r="11"/><circle cx="262" cy="320" r="11"/>
    </g>
    <g stroke="#f3ee6d" stroke-width="1.5">
      <line x1="306" y1="120" x2="350" y2="120"/><line x1="298" y1="176" x2="340" y2="176"/><line x1="290" y1="221" x2="332" y2="221"/><line x1="282" y1="265" x2="324" y2="265"/><line x1="274" y1="320" x2="316" y2="320"/>
    </g>
  </svg>
  <div class="band" style="width:300px;clip-path:polygon(0 0,100% 0,98% 100%,0 100%)">The Method</div>
  <div class="abs copy" style="left:36px;top:75px;width:220px">
    <p class="label" style="font-size:9px;margin-bottom:8px">Introducing the 90-Day Business Accelerator Method</p>
    <p style="margin-bottom:3px">This method works because it focuses on <b>building a system first - not doing more work.</b></p>
    <p style="margin-bottom:0">Most business owners are self-employed inside a job they created.<br>Everything lives in their head.<br>Decisions. Problems. Direction.<br>They mistake movement for achievement and busyness for productivity.<br>This method flips that.<br>Instead of reacting, we identify:</p>
    <ul class="dots" style="margin:8px 0 8px"><li><b>What's working</b></li><li><b>What's broken</b></li><li><b>What's draining time and energy</b></li></ul>
    <p>Then we build systems, leadership, and structure that remove you as the bottleneck - while strengthening your energy, relationships, and life.</p>
  </div>
  <div class="abs" style="left:362px;top:80px;color:#fff;font-size:9.4px;text-transform:uppercase;font-weight:500">The method flow</div>
  <div class="stage" style="left:354px;top:113px;width:190px"><div class="k">Stage 1:</div><b>Diagnose Reality</b><br>Audit time, energy, and team alignment to find the real bottleneck.</div>
  <div class="stage" style="left:346px;top:169px;width:190px"><div class="k">Stage 2:</div><b>Remove Bottlenecks (ADD)</b><br>Automate. Delegate. Delete.</div>
  <div class="stage" style="left:338px;top:214px;width:190px"><div class="k">Stage 3:</div><b>Build Systems, Not Dependence</b><br>Fix processes so people can perform.</div>
  <div class="stage" style="left:330px;top:258px;width:200px"><div class="k">Stage 4:</div><b>Create Clarity &amp; Accountability</b><br>Visual scorecards that prevent fires before they start.</div>
  <div class="stage" style="left:322px;top:313px;width:215px"><div class="k">Stage 5:</div><b>Align Around a North Star</b><br>A vision big enough for your team to grow into.</div>
  <div class="brand">Brightloom</div>
  <div class="folio reverse">4</div>
</section>

<!-- 5 Step 1 -->
<section class="page col-a row-3">
  <svg class="abs" style="left:0;top:0" width="561" height="395" aria-hidden="true"><polygon points="326,0 561,0 561,395 268,395" fill="#ebebeb"/></svg>
  <svg class="step-rail" viewBox="0 0 135 395" aria-hidden="true">
    <rect width="48" height="395" fill="#232323"/>
    <polygon points="40,395 78,395 112,74 76,74" fill="#f3ee6d"/>
    <polygon points="48,78 96,2 140,78" fill="#f3ee6d"/>
    <circle cx="90" cy="100" r="9" fill="#cfcc8a"/><circle cx="79" cy="200" r="9" fill="#cfcc8a"/>
    <circle cx="68" cy="300" r="10" fill="#232323"/><text x="68" y="304" font-family="Inter" font-size="11" font-weight="700" fill="#f3ee6d" text-anchor="middle">1</text>
  </svg>
  <div class="step-tag">STEP 1</div>
  <div class="abs display" style="left:118px;top:30px;font-size:35px;color:var(--ink)">Diagnose /<br>Clarity</div>
  <div class="abs copy" style="left:100px;top:110px;width:200px;text-align:center">
    <p class="label" style="font-size:9px;margin-bottom:14px">Why diagnosis comes first</p>
    <p style="margin-bottom:14px">Skipping diagnosis puts owners into <b>react mode</b>.</p>
    <p style="margin-bottom:14px">Stress releases cortisol.<br>Cortisol lowers decision quality.<br>High emotion = low intelligence.</p>
    <p style="margin-bottom:14px">Work comes home.<br>Frustration spreads.<br>Business and life bleed into each other.</p>
    <p style="margin-bottom:14px">This creates the<br><b>Doom Loop of Entrepreneurship</b>.</p>
    <p>Diagnosis breaks the loop and creates a <b>flywheel</b> instead.</p>
  </div>
  <div class="abs copy" style="left:300px;top:70px;width:240px">
    <p class="label" style="font-size:9px;text-align:center;line-height:1.2;margin-bottom:12px">The 100 units of<br>time &amp; energy audit</p>
    <p style="text-align:center;margin-bottom:12px">For 7 days, you track every 30 minutes of business and personal time.</p>
    <p style="text-align:center;margin-bottom:12px">By day 3-4, most owners realise: "I'm working 10-12 hours a day - but only 2-3 hours are productive."</p>
    <p style="margin-bottom:4px">Tasks are colour-coded:</p>
    <p style="margin-bottom:2px"><span style="color:var(--red)">●</span> <b style="color:var(--red)">Red</b> → drains energy</p>
    <p style="margin-bottom:10px"><span style="color:var(--green)">●</span> <b style="color:var(--green)">Green</b> → creates momentum</p>
    <p style="margin-bottom:4px">From there we:</p>
    <ul class="dots"><li>Re-design the week</li><li>Chunk work intelligently</li><li>Remove low-value tasks</li><li>Automate and delegate using rapid documentation</li></ul>
    <p style="text-align:center;margin-top:10px">Clarity reveals where freedom is hiding.</p>
  </div>
  <div class="brand">Brightloom</div>
  <div class="folio">5</div>
</section>

<!-- 6 Step 2 -->
<section class="page col-b row-3">
  <div class="photo" role="img" aria-label="Photo of a hand placing a yellow sticky note on a planning wall" style="left:326px;top:0;width:235px;height:395px;clip-path:polygon(8% 0,100% 0,100% 100%,0 100%);background:linear-gradient(120deg,#cfd3d2 0%,#aab0ae 50%,#7f8583 100%)"></div>
  <svg class="step-rail" viewBox="0 0 135 395" aria-hidden="true">
    <rect width="48" height="395" fill="#232323"/>
    <polygon points="40,395 78,395 112,74 76,74" fill="#f3ee6d"/>
    <polygon points="48,78 96,2 140,78" fill="#f3ee6d"/>
    <circle cx="90" cy="100" r="9" fill="#cfcc8a"/><circle cx="68" cy="300" r="9" fill="#cfcc8a"/>
    <circle cx="79" cy="200" r="10" fill="#232323"/><text x="79" y="204" font-family="Inter" font-size="11" font-weight="700" fill="#f3ee6d" text-anchor="middle">2</text>
  </svg>
  <div class="step-tag">STEP 2</div>
  <div class="abs display" style="left:124px;top:30px;font-size:35px;color:var(--ink);text-align:center">Prioritise<br><span style="font-size:27px">(The 90-Day Rule)</span></div>
  <div class="abs copy" style="left:110px;top:110px;width:208px">
    <p class="label" style="font-size:9px;margin-bottom:12px">The 90-Day Rule</p>
    <p style="text-align:center;margin-bottom:12px">Most owners try to fix marketing, hiring, or growth too early - before fixing themselves, their time, and their systems.</p>
    <p style="text-align:center">When everything is a priority, nothing moves.</p>
  </div>
  <div class="abs ink" style="left:92px;top:210px;width:240px;height:86px;clip-path:polygon(4% 0,100% 0,100% 100%,0 100%);padding:13px 0 0 40px">
    <div style="color:var(--yellow);font-weight:800;font-size:12px;margin-bottom:6px">THE RULE:</div>
    <ul class="dots on-dark"><li style="font-weight:700">One Primary Priority</li><li style="font-weight:700">One Secondary Support Priority</li><li style="font-weight:700">Everything else waits</li></ul>
  </div>
  <div class="abs copy" style="left:76px;top:324px;width:250px;text-align:center">Focus turns effort into results.</div>
  <div class="brand">Brightloom</div>
  <div class="folio">6</div>
</section>

<!-- 7 Step 3 -->
<section class="page col-a row-4">
  <svg class="abs" style="left:0;top:0" width="561" height="395" aria-hidden="true"><polygon points="326,0 561,0 561,395 268,395" fill="#ebebeb"/></svg>
  <div class="photo" role="img" aria-label="Photo of a stressed business owner holding his head" style="left:72px;top:250px;width:208px;height:145px;clip-path:polygon(0 0,100% 0,96% 100%,0 100%);background:linear-gradient(135deg,#d8d8d6 0%,#b7b3ad 55%,#8e8a84 100%)"></div>
  <svg class="step-rail" viewBox="0 0 135 395" aria-hidden="true">
    <rect width="48" height="395" fill="#232323"/>
    <polygon points="40,395 78,395 112,74 76,74" fill="#f3ee6d"/>
    <polygon points="48,78 96,2 140,78" fill="#f3ee6d"/>
    <circle cx="79" cy="200" r="9" fill="#cfcc8a"/><circle cx="68" cy="300" r="9" fill="#cfcc8a"/>
    <circle cx="90" cy="100" r="10" fill="#232323"/><text x="90" y="104" font-family="Inter" font-size="11" font-weight="700" fill="#f3ee6d" text-anchor="middle">3</text>
  </svg>
  <div class="step-tag">STEP 3</div>
  <div class="abs display" style="left:118px;top:30px;font-size:35px;color:var(--ink)">Execute with<br>Guidance</div>
  <div class="abs copy" style="left:108px;top:112px;width:190px">
    <p class="label" style="font-size:9px;line-height:1.2;margin-bottom:12px">Information isn't the<br>problem</p>
    <p style="text-align:center;margin-bottom:10px">Everyone has access to information.<br>Information without guidance leads to:</p>
    <ul class="dots"><li>Overwhelm</li><li>Inaction</li><li>Starting and stopping</li></ul>
  </div>
  <div class="abs copy" style="left:308px;top:70px;width:230px">
    <p class="label" style="font-size:9px;margin-bottom:10px">State → Story → Strategy</p>
    <p style="text-align:center;margin-bottom:8px">If you're in a bad state, you tell yourself bad stories:</p>
    <ul class="dots"><li>"I've tried this before."</li><li>"This won't work for me."</li><li>"Everyone I know is struggling."</li><li>"That's just how business is."</li></ul>
    <p style="text-align:center;margin:8px 0 12px">That story feels logical - but it's bullshit.</p>
    <p style="margin-bottom:6px">Execution requires:</p>
    <ul class="dots"><li>The right state</li><li>The right story</li><li>The right sequence</li><li>The right environment</li></ul>
    <p style="text-align:center;margin-top:10px">That's where momentum is built.</p>
  </div>
  <div class="brand">Brightloom</div>
  <div class="folio">7</div>
</section>

<!-- 8 Feedback loop -->
<section class="page col-b row-4">
  <div class="photo" role="img" aria-label="Photo of a hand placing a dart in the bullseye of a target" style="left:300px;top:0;width:261px;height:238px;background:radial-gradient(circle at 40% 70%,#6c6c6c 0%,#3f3f3f 40%,#cfd2d2 100%)"></div>
  <svg class="abs" style="left:0;top:0" width="561" height="395" aria-hidden="true">
    <polygon points="302,236 561,236 561,395 280,395" fill="#2b2b2b"/>
  </svg>
  <div class="band" style="width:305px;clip-path:polygon(0 0,100% 0,98% 100%,0 100%)">The Feedback Loop</div>
  <div class="abs label" style="left:36px;top:82px;font-size:9.6px;font-weight:600">Review → Refine → Scale</div>
  <div class="abs copy" style="left:36px;top:128px;width:100px">Sustainable growth starts with reviewing the owner first:</div>
  <div class="abs yellow" style="left:146px;top:107px;width:155px;height:92px;clip-path:polygon(6% 0,100% 0,100% 100%,0 100%);padding:8px 0 0 22px">
    <ul class="dots"><li>Sleep</li><li>Energy</li><li>Health</li><li>Mental space</li></ul>
  </div>
  <svg class="abs" style="left:0;top:0" width="561" height="395" aria-hidden="true">
    <polygon points="206,199 222,199 214,209" fill="#f3ee6d"/>
    <circle cx="282" cy="141" r="19" fill="#fff" stroke="#232323" stroke-width="3"/><circle cx="282" cy="141" r="7" fill="#232323"/>
    <circle cx="264" cy="227" r="19" fill="#fff" stroke="#232323" stroke-width="3"/>
    <polyline points="255,234 262,226 268,230 275,219" fill="none" stroke="#232323" stroke-width="2.5"/>
  </svg>
  <div class="abs copy" style="left:36px;top:238px">Then the business:</div>
  <div class="abs yellow" style="left:132px;top:211px;width:142px;height:86px;clip-path:polygon(6% 0,100% 0,100% 100%,0 100%);padding:15px 0 0 20px">
    <ul class="dots"><li>Annual vision</li><li>Quarterly priorities</li><li>Weekly scorecards</li></ul>
  </div>
  <div class="abs copy" style="left:36px;top:319px">Most owners are stuck being Captain Valor - the hero.</div>
  <div class="abs copy light" style="left:330px;top:258px;width:200px">
    <p style="margin-bottom:8px">Real leaders become <b>Wexford</b>:</p>
    <ul class="dots on-dark" style="padding-left:2px"><li>They set the mission</li><li>Create structure</li><li>Empower execution</li></ul>
    <p style="margin-top:6px">That's how scale becomes repeatable.</p>
  </div>
  <div class="brand">Brightloom</div>
  <div class="folio reverse">8</div>
</section>

<!-- 9 Method in action -->
<section class="page col-a row-5">
  <svg class="abs" style="left:0;top:0" width="561" height="395" aria-hidden="true">
    <polygon points="314,0 561,0 561,395 290,395" fill="#2b2b2b"/>
    <rect x="0" y="0" width="561" height="56" fill="#232323"/>
  </svg>
  <div class="abs display" style="left:36px;top:13px;font-size:30px;color:#fff;font-weight:800">The Method in Action <span style="margin-left:14px">(Anonymised)</span></div>
  <div class="abs copy" style="left:36px;top:78px;width:200px">
    <p style="margin-bottom:10px">A trades business owner looked successful<br>- but was exhausted.</p>
    <p style="margin-bottom:10px">Everything depended on him.</p>
    <p style="margin-bottom:10px">Home life suffered.</p>
    <p>Energy collapsed.</p>
  </div>
  <div class="abs copy light" style="left:340px;top:138px;width:182px;text-align:right">
    <p>The business didn't change first.</p><p><b>The leader did.</b></p>
  </div>
  <div class="stat-card" style="left:52px;top:202px;width:146px;height:142px;clip-path:polygon(6% 0,100% 0,100% 100%,0 100%)">
    <p class="copy">We started with him:</p>
    <ul class="dots"><li>Reset energy and mindset</li><li>Rebuilt vision and boundaries</li><li>Installed systems and standards</li></ul>
  </div>
  <div class="stat-card" style="left:190px;top:202px;width:146px;height:142px;clip-path:polygon(6% 0,100% 0,100% 100%,0 100%)">
    <p class="copy">Within 90 days:</p>
    <ul class="dots"><li>Energy returned</li><li style="margin-top:10px">Marriage reconnected</li><li style="margin-top:10px">Revenue increased by ~$30,000 per month</li></ul>
  </div>
  <div class="stat-card" style="left:328px;top:202px;width:180px;height:142px;clip-path:polygon(6% 0,100% 0,100% 100%,0 100%)">
    <p class="copy">Two years later:</p>
    <ul class="dots"><li>Revenue tripled</li><li>Business runs without him</li><li>Multiple family holidays per year</li><li>He goes to work because he wants to</li></ul>
  </div>
  <div class="brand">Brightloom</div>
  <div class="folio reverse">9</div>
</section>

<!-- 10 Common mistakes -->
<section class="page col-b row-5 yellow">
  <svg class="abs" style="left:0;top:0" width="561" height="395" aria-hidden="true"><polygon points="272,0 561,0 561,395 212,395" fill="#2b2b2b"/></svg>
  <div class="abs display" style="left:60px;top:30px;font-size:56px;color:var(--ink)">Common</div>
  <div class="abs display" style="left:282px;top:30px;font-size:56px;color:var(--yellow)">Mistakes</div>
  <ol class="abs num-list" style="left:36px;top:104px;width:200px">
    <li><span>1</span>Scaling before the business is stable without you</li>
    <li><span>2</span>Confusing busyness with progress</li>
    <li><span>3</span>Fixing tactics instead of fixing the owner</li>
    <li><span>4</span>Hiring before systems exist</li>
    <li><span>5</span>Tolerating "good enough" staff or clients</li>
    <li><span>6</span>No review cadence</li>
    <li><span>7</span>Trying to do it alone</li>
  </ol>
  <div class="abs" style="left:290px;top:156px;width:232px;color:#fff;font-size:14.4px;font-weight:500;text-transform:uppercase;text-align:right;line-height:1.6;letter-spacing:.2px">Most owners don't fail - they compound the wrong decisions for too long.</div>
  <div class="brand">Brightloom</div>
  <div class="folio reverse">10</div>
</section>

<!-- 11 What this method does -->
<section class="page col-a row-6">
  <div class="photo" role="img" aria-label="Soft-focus photo of a glass sphere held over water" style="left:0;top:54px;width:300px;height:341px;background:linear-gradient(180deg,#dfe4e7 0%,#c9d0d4 45%,#b6bbbd 100%)"></div>
  <svg class="abs" style="left:0;top:0" width="561" height="395" aria-hidden="true">
    <polygon points="302,0 561,0 561,395 244,395" fill="#f3ee6d"/>
    <polygon points="296,54 561,54 561,134 286,134" fill="#232323"/>
  </svg>
  <div class="band" style="width:302px">What this method does</div>
  <div class="abs display" style="left:334px;top:70px;font-size:25px;color:#fff;font-weight:800;line-height:1.1">What this method<br>does <span style="color:var(--yellow)">not</span> do</div>
  <ul class="abs dots big" style="left:36px;top:178px"><li>Creates clarity</li><li>Removes you as the bottleneck</li><li>Builds systems that scale</li><li>Reclaims 20-30 hours per week</li></ul>
  <ul class="abs dots big" style="left:318px;top:178px"><li>Provide a quick fix</li><li>Work without execution</li><li>Replace personal responsibility</li></ul>
  <div class="abs" style="left:292px;top:320px;font-size:11px;font-weight:700;color:var(--ink)">This is a method - not a miracle.</div>
  <div class="brand">Brightloom</div>
  <div class="folio">11</div>
</section>

<!-- 12 How Brightloom fits -->
<section class="page col-b row-6">
  <svg class="abs" style="left:0;top:0" width="561" height="395" aria-hidden="true"><polygon points="314,54 561,54 561,395 276,395" fill="#2b2b2b"/></svg>
  <div class="band" style="width:561px">How Brightloom fits</div>
  <div class="abs" style="left:36px;top:108px;width:250px;font-size:11px;line-height:1.35;color:var(--text)">
    <p style="margin-bottom:14px"><b style="font-weight:800;letter-spacing:.3px">BRIGHTLOOM</b> helps business owners recreate the life they once had in their head.</p>
    <p style="margin-bottom:14px">You're surrounded by people who:</p>
  </div>
  <ul class="abs dots big" style="left:36px;top:186px"><li>Share real numbers</li><li>Speak honestly about business and life</li><li>Solve problems in real time</li></ul>
  <div class="abs" style="left:354px;top:100px;color:#fff;font-size:11px;font-weight:600">You get:</div>
  <ul class="abs dots big on-dark" style="left:340px;top:132px;width:190px"><li>Actionable models</li><li>Expert guidance</li><li>Life + business integration</li><li>In-person events where family is part of the journey</li></ul>
  <div class="abs" style="left:330px;top:320px;color:#fff;font-size:11px;font-weight:600">Environment changes outcomes.</div>
  <div class="brand">Brightloom</div>
  <div class="folio reverse">12</div>
</section>

<!-- 13 Your next step -->
<section class="page col-a row-7">
  <svg class="abs" style="left:0;top:0" width="561" height="395" aria-hidden="true">
    <polygon points="262,0 561,0 561,395 180,395" fill="#2b2b2b"/>
    <polygon points="52,38 224,38 224,12 290,56 224,100 224,74 52,74" fill="#f3ee6d"/>
  </svg>
  <div class="abs display" style="left:50px;top:112px;font-size:64px;color:var(--ink);line-height:.9">Your<br>Next<br>Step</div>
  <div class="abs display" style="left:300px;top:40px;font-size:26px;color:#fff;font-weight:800">Book a <span style="color:var(--yellow)">Clarity Call</span></div>
  <div class="abs" style="left:268px;top:98px;width:270px;color:#fff;font-size:11px;font-weight:600;line-height:1.3">
    <p style="margin-bottom:12px">This is not a sales call.</p>
    <p style="margin-bottom:12px">On this call:</p>
  </div>
  <ul class="abs dots big on-dark" style="left:256px;top:160px;width:270px"><li style="margin-bottom:12px">We identify your real bottleneck</li><li style="margin-bottom:12px">Provide personalised, actionable steps</li><li style="margin-bottom:12px">Align business goals with personal and family goals</li></ul>
  <div class="abs" style="left:238px;top:270px;width:270px;color:#fff;font-size:11px;font-weight:600;line-height:1.3">Brightloom is application-only to protect culture and standards.</div>
  <div class="abs" style="left:300px;top:328px;width:222px;color:#fff;font-size:14px;font-weight:500;text-align:right;line-height:1.3">CLARITY FIRST.<br>DECISIONS SECOND.</div>
  <div class="brand">Brightloom</div>
  <div class="folio reverse">13</div>
</section>

<!-- 14 Closing -->
<section class="page col-b row-7 ink">
  <div class="photo" role="img" aria-label="Photo of a man in a cap looking up at a bright sky" style="left:0;top:0;width:300px;height:395px;clip-path:polygon(0 0,100% 0,82% 100%,0 100%);background:linear-gradient(160deg,#a9c6d6 0%,#c9b79a 45%,#6b5a48 100%)"></div>
  <svg class="abs" style="left:0;top:0" width="561" height="395" aria-hidden="true">
    <polygon points="36,306 238,306 238,282 274,322 238,362 238,338 36,338" fill="#f3ee6d"/>
  </svg>
  <div class="abs" style="left:294px;top:66px;width:240px;color:#fff;font-size:11px;font-weight:600;line-height:1.3">
    <p style="margin-bottom:14px">You didn't start a business to feel trapped.</p>
    <p style="margin-bottom:14px">You did it for freedom.<br>For family.<br>For choice.</p>
    <p style="margin-bottom:14px">The problem isn't you. The problem is no one showed you the correct sequence.</p>
    <p>The 90-Day Business Accelerator Method is about doing what matters - in the right order - with the right support.</p>
  </div>
  <div class="abs" style="left:280px;top:306px;width:252px;color:#fff;font-size:14px;font-weight:500;text-align:right;line-height:1.5">A BUSINESS SHOULD SERVE YOUR LIFE - NOT CONSUME IT.</div>
  <div class="brand">Brightloom</div>
  <div class="folio reverse">14</div>
</section>

</main>
</body>
</html>
```